Dufresne Roofing

Want a professional looking business card

Industry/Entity Type

Business

Contact Information for Business Card

Marc Dufresne ( Owner) marc@dufresneroofing-example.com, www.dufresneroofing-example.com, Adress: 4217 County road 42 Wendover,ON K0A3M1

```html
<!DOCTYPE html>
<html lang="en">
<head>
<meta charset="utf-8">
<title>Dufresne Roofing – Business Card</title>
<link rel="stylesheet" href="https://fonts.googleapis.com/css2?family=Open+Sans:wght@400;600;700&display=swap">
<style>
  :root {
    --backdrop: #2b2b2d;
    --card-white: #ffffff;
    --card-grey: #7b7c7e;
    --brand-blue: #1f4189;
    --brand-blue-dark: #17336f;
    --silver: #b9bbbe;
    --text-grey: #6d6e71;
    --pale-grey: #e9eaec;
  }
  * { box-sizing: border-box; margin: 0; padding: 0; }
  html, body { width: 1200px; height: 900px; overflow: hidden; }
  body {
    background: var(--backdrop);
    font-family: "Open Sans", Arial, sans-serif;
    position: relative;
  }
  .card {
    position: absolute;
    width: 520px;
    height: 300px;
    overflow: hidden;
    box-shadow: 0 10px 24px rgba(0,0,0,.45);
  }

  /* Back side */
  .card-back { left: 90px; top: 150px; background: var(--card-grey); }
  .card-back .wordmark {
    position: absolute; left: 0; right: 0; top: 100px;
    text-align: center; color: var(--card-white);
    font-weight: 700; font-size: 36px; letter-spacing: 1px;
  }
  .card-back .web-rule {
    position: absolute; left: 40px; right: 40px; top: 220px;
    display: flex; align-items: center; gap: 10px;
    color: var(--card-white); font-size: 13px;
  }
  .card-back .web-rule::before,
  .card-back .web-rule::after {
    content: ""; flex: 1; height: 1px; background: rgba(255,255,255,.7);
  }

  /* Front side */
  .card-front { left: 590px; top: 450px; background: var(--card-white); }
  .card-front .house-decoration {
    position: absolute; left: 400px; top: 215px; width: 110px; height: 85px;
    background: linear-gradient(180deg, var(--pale-grey), rgba(233,234,236,.35));
  }
  .card-front .swoosh { position: absolute; inset: 0; }
  .card-front .holder {
    position: absolute; right: 44px; top: 40px; width: 190px;
    text-align: center; color: var(--card-white);
  }
  .holder .holder-name { font-weight: 700; font-size: 19px; }
  .holder .holder-role { font-size: 12px; margin-top: 2px; }
  .card-front .wordmark {
    position: absolute; left: 24px; top: 118px;
    color: var(--brand-blue); font-weight: 700; font-size: 26px;
    display: flex; align-items: center; gap: 10px;
  }
  .wordmark .mark-square {
    width: 16px; height: 16px; background: var(--brand-blue);
  }
  .contact {
    position: absolute; left: 24px; top: 196px;
    font-size: 11.5px; line-height: 15px; color: var(--text-grey);
  }
  .contact .company { color: var(--brand-blue); font-size: 12.5px; }
  .contact-lines { display: flex; gap: 7px; margin-top: 3px; }
  .contact-icons { display: flex; flex-direction: column; gap: 1px; }
  .contact-icons svg { width: 14px; height: 14px; display: block; }
</style>
</head>
<body>

  <section class="card card-back" aria-label="Business card, back">
    <div class="wordmark">Dufresne Roofing</div>
    <div class="web-rule">www.dufresneroofing-example.com</div>
  </section>

  <section class="card card-front" aria-label="Business card, front">
    <div class="house-decoration" role="img" aria-label="Faint house outline decoration"></div>

    <svg class="swoosh" viewBox="0 0 520 300" width="520" height="300" aria-hidden="true">
      <defs>
        <linearGradient id="blueBand" x1="0" y1="0" x2="1" y2="1">
          <stop offset="0" stop-color="var(--brand-blue)"/>
          <stop offset="1" stop-color="var(--brand-blue-dark)"/>
        </linearGradient>
      </defs>
      <path d="M272 0 C300 40 290 100 360 128 C420 150 480 180 520 230 V262 C470 205 410 175 345 160 C280 145 280 60 264 0 Z" fill="var(--silver)"/>
      <path d="M290 0 H520 V222 C480 180 430 150 370 135 C300 115 310 40 290 0 Z" fill="url(#blueBand)"/>
    </svg>

    <div class="holder">
      <div class="holder-name">Marc Dufresne</div>
      <div class="holder-role">Owner</div>
    </div>

    <div class="wordmark"><span class="mark-square"></span>Dufresne Roofing</div>

    <div class="contact">
      <div class="company">Dufresne Roofing</div>
      <div>4217 County road 42,</div>
      <div>Wendover,ON K0A3M1</div>
      <div class="contact-lines">
        <div class="contact-icons">
          <svg viewBox="0 0 14 14" aria-hidden="true"><rect width="14" height="14" fill="var(--brand-blue)"/><path d="M4 3 L6 3 L6.6 5 L5.5 6 C6 7.3 6.8 8.1 8 8.5 L9 7.4 L11 8 L11 10 C7 10.5 3.5 7 4 3 Z" fill="#fff"/></svg>
          <svg viewBox="0 0 14 14" aria-hidden="true"><rect width="14" height="14" fill="var(--brand-blue)"/><rect x="3" y="4.5" width="8" height="5.5" fill="none" stroke="#fff" stroke-width="1"/><path d="M3 4.5 L7 7.5 L11 4.5" fill="none" stroke="#fff" stroke-width="1"/></svg>
          <svg viewBox="0 0 14 14" aria-hidden="true"><rect width="14" height="14" fill="var(--brand-blue)"/><circle cx="7" cy="7" r="4" fill="none" stroke="#fff" stroke-width="1"/><ellipse cx="7" cy="7" rx="1.8" ry="4" fill="none" stroke="#fff" stroke-width=".8"/><line x1="3" y1="7" x2="11" y2="7" stroke="#fff" stroke-width=".8"/></svg>
        </div>
        <div>
          <div>(613) 555-0142</div>
          <div>marc@dufresneroofing-example.com</div>
          <div>www.dufresneroofing-example.com</div>
        </div>
      </div>
    </div>
  </section>

</body>
</html>
```